Book cover for dissertation on learning in start-up teams

I am looking for a book cover (front, back, side) for publishing my phd project in A5 format. My phd Investigated the effects of learning (eg, reflection as a team, participation in team trainings) in start-up management teams on the performance and the satisfaction of synthesis teams. The front and side of the cover shoulderstand contain the name of the dissertation and my name, the back a short summary (see attachement). I am open with regard to the type of design (eg, photo, sketch, drawing) and with regard to the colors, etc.

Target Market(s)

Scientific community / Researchers and readers did are interested in team research

Industry/Entity Type

Learning

Requirements
Must have
• A5 format / pdf format / front, back, side

```html
<!DOCTYPE html>
<html lang="en">
<head>
<meta charset="utf-8">
<title>Learning in Founding Teams – Cover</title>
<link href="https://fonts.googleapis.com/css2?family=Roboto:wght@300;400;700&family=EB+Garamond:wght@400&display=swap" rel="stylesheet">
<style>
  :root {
    --paper: #cbb99a;
    --band: #f6b333;
    --spine: #a6897a;
    --ink: #111111;
    --white: #ffffff;
    --art: #dccdb2;
  }
  * { margin: 0; padding: 0; box-sizing: border-box; }
  html, body { width: 1200px; height: 837px; overflow: hidden; background: var(--paper); }
  .cover { position: relative; width: 1200px; height: 837px; background: var(--paper); font-family: "Roboto", Arial, sans-serif; color: var(--ink); }

  /* Back */
  .back { position: absolute; left: 0; top: 0; width: 590px; height: 837px; }
  .back-title { position: absolute; left: 72px; top: 118px; color: var(--white); font-weight: 700; font-size: 16.5px; line-height: 20px; letter-spacing: -0.2px; }
  .back-subtitle { position: absolute; left: 72px; top: 179px; color: var(--ink); font-weight: 300; font-size: 17px; line-height: 20.5px; }
  .abstract { position: absolute; left: 73px; width: 238px; }
  .abstract h2 { font-family: "Roboto", Arial, sans-serif; font-weight: 700; font-size: 10.5px; margin-bottom: 1px; }
  .abstract p { font-family: "EB Garamond", Georgia, serif; font-size: 10.6px; line-height: 13.5px; text-align: justify; }
  .abstract-en { top: 296px; }
  .abstract-de { top: 472px; }
  .signature { position: absolute; right: 280px; font-family: "EB Garamond", Georgia, serif; font-size: 10px; text-align: right; white-space: nowrap; }
  .signature-label { top: 688px; }
  .signature-name { top: 743px; }

  /* Spine */
  .spine { position: absolute; left: 590px; top: 0; width: 20px; height: 837px; background: var(--spine); }
  .spine-text { position: absolute; left: 10px; top: 419px; transform: translate(-50%, -50%) rotate(-90deg); white-space: nowrap; color: var(--white); font-weight: 700; font-size: 10px; letter-spacing: 0.05px; }

  /* Front */
  .front { position: absolute; left: 610px; top: 0; width: 590px; height: 837px; }
  .institution { position: absolute; left: 0; top: 0; width: 590px; height: 120px; background: var(--band); text-align: center; font-size: 13px; line-height: 15px; font-weight: 300; padding-top: 24px; }
  .institution .name { font-weight: 700; font-size: 14px; }
  .institution .dept { margin-top: 13px; }
  .front-title { position: absolute; left: 43px; top: 140px; color: var(--white); font-weight: 700; font-size: 48px; line-height: 50px; letter-spacing: -1.6px; }
  .front-subtitle { position: absolute; left: 43px; top: 249px; font-weight: 300; font-size: 25px; line-height: 30.5px; }
  .illustration { position: absolute; left: 66px; top: 388px; width: 456px; height: 214px; background: var(--art); border-radius: 40px; }
  .author { position: absolute; left: 0; width: 590px; top: 634px; text-align: center; font-size: 24px; font-weight: 300; letter-spacing: -0.3px; }
  .author strong { font-weight: 700; }
  .committee { position: absolute; left: 43px; top: 744px; font-size: 16px; line-height: 20.5px; display: grid; grid-template-columns: 206px auto; font-weight: 300; }
  .committee dt { font-weight: 700; }
</style>
</head>
<body>
<div class="cover">
  <section class="back">
    <h1 class="back-title">LEARNING<br>IN FOUNDING TEAMS:</h1>
    <p class="back-subtitle">The Effect of Learning Behavior<br>and a Team Intervention<br>on Team Processes<br>and Outcomes</p>
    <div class="abstract abstract-en">
      <h2>Short abstract</h2>
      <p>Drawing on two quantitative longitudinal studies, this dissertation demonstrates the effects of informal and formal learning activities on team outcomes in founding teams and the mediating role of teamwork quality. The effect of formal learning is shown to be contingent on the extent of prior informal learning. Moreover, this dissertation illustrates how formal learning activities in form of a team intervention for founding teams should be designed and implemented. The results contribute to diverse related areas of research.</p>
    </div>
    <div class="abstract abstract-de" lang="de">
      <h2>Kurze Zusammenfassung</h2>
      <p>Aufbauend auf zwei quantitativen Studien zeigt diese Dissertation die Wirkung von informalem und formalem Lernen auf Teamergebnisse in Gründerteams und beleuchtet, welche Rolle gute Arbeitspraktiken im Team als vermittelnder Mechanismus spielen. Der Effekt des formalen Lernens hängt dabei von dem Ausmaß des vorherigen informalen Lernens ab. Zudem erläutert diese Dissertation, wie formales Lernen in Form einer Intervention für Gründerteams konzipiert und durchgeführt werden sollte. Die Ergebnisse leisten Beiträge zu verschiedenen verwandten Forschungszweigen.</p>
    </div>
    <p class="signature signature-label">Unterschrift</p>
    <p class="signature signature-name">(Prof. Dr. Dr. Keller)</p>
  </section>

  <section class="spine">
    <p class="spine-text">LEARNING IN FOUNDING TEAMS: THE EFFECT OF LEARNING BEHAVIOR AND A TEAM INTERVENTION ON TEAM PROCESSES AND OUTCOMES - LENA BERGER</p>
  </section>

  <section class="front">
    <header class="institution">
      <div class="name">TECHNISCHE UNIVERSITÄT NORDSTADT</div>
      <div>Fakultät für Wirtschaftswissenschaften</div>
      <div class="dept">Department of Venture Development<br>and Strategy/New Venture Formation Research Center</div>
    </header>
    <h1 class="front-title">LEARNING<br>IN FOUNDING TEAMS:</h1>
    <p class="front-subtitle">The Effect of Learning Behavior<br>and a Team Intervention<br>on Team Processes<br>and Outcomes</p>
    <div class="illustration" role="img" aria-label="White abstract line drawing of three playful figures formed from dots and curved strokes"></div>
    <p class="author">Lena<strong>Berger</strong></p>
    <dl class="committee">
      <dt>Vorsitzender:</dt><dd>1. Prof. Dr. Tobias Lindner</dd>
      <dt>Prüfer der Dissertation:</dt><dd>1. Prof. Dr. Dr. Martin Keller</dd>
      <dt></dt><dd>2. Prof. Dr. Clara Weiss</dd>
    </dl>
  </section>
</div>
</body>
</html>
```